Infographic for Labor Trends - Supply Chain Theme

Looking to polish this slide up to look professional enough to share with the Board of Directors. The focus is Supply Chain Labor (Warehousing and transportation) Need to have a theme around Supply Chain workforce. Needs to be formatted for wide screen PowerPoint

```html
<!DOCTYPE html>
<html lang="en">
<head>
<meta charset="utf-8">
<title>Supply Chain Job Market Remains Tight</title>
<link href="https://fonts.googleapis.com/css2?family=PT+Sans:wght@400;700&family=Open+Sans:wght@400;600;700&display=swap" rel="stylesheet">
<style>
  :root {
    --canvas: #b5b5b5;
    --slide: #ffffff;
    --panel: #efefef;
    --ink: #333333;
    --title: #555555;
    --muted: #6b6b6b;
    --red: #c8102e;
    --bar-gray: #a6a6a6;
    --rule: #d9d9d9;
    --navy: #1f3f8f;
    --teal: #2e8b6f;
    --magenta: #c33a93;
    --amber: #c98a2a;
  }
  * { box-sizing: border-box; margin: 0; padding: 0; }
  html, body { width: 1045px; height: 1200px; overflow: hidden; }
  body { background: var(--canvas); position: relative; font-family: "Open Sans", Arial, sans-serif; color: var(--ink); }

  .slide {
    position: absolute; left: 84px; width: 878px; height: 493px;
    background: var(--slide); box-shadow: 0 1px 4px rgba(0,0,0,.25); overflow: hidden;
  }
  .slide--first { top: 53px; }
  .slide--second { top: 596px; }
  .side-panel { position: absolute; left: 546px; top: 0; width: 332px; height: 493px; background: var(--panel); }
  .slide--second .side-panel { background: transparent; }

  .slide-title {
    position: absolute; left: 41px; top: 18px;
    font-family: "PT Sans", Arial, sans-serif; font-weight: 700; font-size: 24px;
    color: var(--title); letter-spacing: .2px;
  }
  .title-rule { position: absolute; left: 41px; top: 56px; height: 1px; background: var(--red); }
  .slide--first .title-rule { width: 505px; }
  .slide--second .title-rule { width: 827px; }
  .page-number { position: absolute; right: 12px; top: 10px; font-size: 9px; color: #999; }

  .key-points { position: absolute; left: 41px; top: 70px; width: 490px; list-style: none; }
  .key-points li { position: relative; padding-left: 13px; font-size: 12.6px; line-height: 17px; margin-bottom: 5px; color: var(--ink); }
  .key-points li::before { content: "•"; position: absolute; left: 0; top: 0; }

  .sector-chart { position: absolute; left: 0; top: 225px; }
  .chart-heading { font-family: "Open Sans", Arial, sans-serif; }

  .brand-name {
    position: absolute; left: 44px; top: 467px;
    font-family: "Open Sans", Arial, sans-serif; font-weight: 700; font-size: 10px; color: var(--red);
  }

  .trend-block { position: absolute; left: 575px; top: 72px; width: 290px; }
  .trend-title { font-weight: 700; font-size: 9.6px; color: var(--ink); }
  .trend-sub { font-size: 9.6px; color: var(--muted); line-height: 13px; }
  .trend-note { margin-top: 6px; font-size: 7.4px; line-height: 10.4px; color: var(--muted); }

  .postings-chart { position: absolute; left: 575px; top: 172px; }
  .incentive-chart { position: absolute; left: 575px; top: 336px; }
  svg text { font-family: "Open Sans", Arial, sans-serif; }
</style>
</head>
<body>

<!-- Slide A -->
<section class="slide slide--first">
  <div class="side-panel"></div>
  <h1 class="slide-title">SUPPLY CHAIN JOB MARKET REMAINS TIGHT</h1>
  <div class="title-rule"></div>
  <span class="page-number">7</span>
  <ul class="key-points">
    <li>We continue to see pressure and struggle to attract the talent needed to meet staffing demands in multiple markets</li>
    <li>Wage inflation in the industry continues and is amplified lack of talent to cover demand for the holiday season cycle</li>
    <li>We expect demand to remain extremely high through 2022 period due to the amount of backlog freight at the ports and missed Holiday placement of goods</li>
  </ul>

  <svg class="sector-chart" width="560" height="268" viewBox="0 0 560 268">
    <text x="41" y="10" font-size="8.4" font-weight="700" fill="#333">Some sectors are booming while others lag</text>
    <text x="41" y="21" font-size="8" fill="#555">% change in US job postings, seasonally adjusted, Oct 8, 2021</text>
    <g font-size="7" font-weight="700" fill="#c8102e" text-anchor="middle">
      <text x="62.5" y="41">9.0%</text><text x="94.5" y="51">4.1%</text><text x="125.5" y="50">6.2%</text><text x="156.5" y="49">7.5%</text>
      <text x="232.5" y="44">7.0%</text><text x="263.5" y="47">6.0%</text><text x="294.5" y="69">2.8%</text><text x="326.5" y="88">0.7%</text>
      <text x="406.5" y="41">1.6%</text><text x="437.5" y="46">2.1%</text><text x="469.5" y="78">2.4%</text>
    </g>
    <g fill="#c8102e">
      <rect x="52" y="44" width="21" height="13"/><rect x="84" y="54" width="21" height="7"/><rect x="115" y="53" width="21" height="9"/><rect x="146" y="52" width="21" height="10"/>
      <rect x="222" y="47" width="21" height="17"/><rect x="253" y="50" width="21" height="15"/><rect x="284" y="72" width="21" height="6"/><rect x="316" y="91" width="21" height="2"/>
      <rect x="396" y="44" width="21" height="11"/><rect x="427" y="49" width="21" height="13"/><rect x="459" y="81" width="21" height="17"/>
      <rect x="491" y="203" width="21" height="29"/>
    </g>
    <g fill="#a6a6a6">
      <rect x="52" y="57" width="21" height="127"/><rect x="84" y="61" width="21" height="123"/><rect x="115" y="62" width="21" height="122"/><rect x="146" y="62" width="21" height="122"/>
      <rect x="222" y="64" width="21" height="120"/><rect x="253" y="65" width="21" height="119"/><rect x="284" y="78" width="21" height="106"/><rect x="316" y="93" width="21" height="91"/>
      <rect x="396" y="55" width="21" height="129"/><rect x="427" y="62" width="21" height="122"/><rect x="459" y="98" width="21" height="86"/>
      <rect x="491" y="186" width="21" height="17"/>
    </g>
    <g font-size="4.6" fill="#333" text-anchor="middle">
      <text x="62.5" y="124">92.9%</text><text x="94.5" y="124">89.9%</text><text x="125.5" y="124">89.4%</text><text x="156.5" y="124">89%</text>
      <text x="232.5" y="124">51.4%</text><text x="263.5" y="124">50.6%</text><text x="294.5" y="124">44.4%</text><text x="326.5" y="124">38.7%</text>
      <text x="406.5" y="124">22.0%</text><text x="437.5" y="124">18.6%</text><text x="469.5" y="124">13.2%</text>
      <text x="501.5" y="197">-3.8%</text>
      <text x="501.5" y="221" fill="#fff">-3.1%</text>
    </g>
    <g font-size="4.8" fill="#fff">
      <text transform="translate(64.5 180) rotate(-90)">Human Resources</text>
      <text transform="translate(96.5 180) rotate(-90)">Production &amp; Mfg</text>
      <text transform="translate(127.5 180) rotate(-90)">Loading &amp; Stocking</text>
      <text transform="translate(158.5 180) rotate(-90)">Pharmacy</text>
      <text transform="translate(234.5 180) rotate(-90)">Driving</text>
      <text transform="translate(265.5 180) rotate(-90)">Childcare</text>
      <text transform="translate(296.5 180) rotate(-90)">Arts &amp; Entertainment</text>
      <text transform="translate(328.5 180) rotate(-90)">Food Prep &amp; Service</text>
      <text transform="translate(408.5 180) rotate(-90)">Cleaning</text>
      <text transform="translate(439.5 180) rotate(-90)">Hospitality &amp; Tourism</text>
      <text transform="translate(471.5 180) rotate(-90)">Education</text>
      <text transform="translate(503.5 180) rotate(-90)" fill="#555">Beauty &amp; Wellness</text>
    </g>
    <g stroke="#999" stroke-width=".8">
      <line x1="45" y1="186" x2="175" y2="186"/><line x1="215" y1="186" x2="345" y2="186"/><line x1="388" y1="186" x2="520" y2="186"/>
    </g>
    <g font-size="5.8" font-weight="700" fill="#c8102e" text-anchor="middle">
      <text x="110" y="196">Better than economy average</text>
      <text x="280" y="196">Similar to economy average</text>
      <text x="453" y="196">Worse than economy average</text>
    </g>
    <rect x="272" y="225" width="6" height="6" fill="#a6a6a6"/>
    <text x="281" y="230.5" font-size="5.6" fill="#555">% change since 2/1/20</text>
    <rect x="350" y="225" width="6" height="6" fill="#c8102e"/>
    <text x="359" y="230.5" font-size="5.6" fill="#555">% pt. change vs 4 weeks ago</text>
  </svg>

  <div class="brand-name">Harbor Supply Co.</div>

  <div class="trend-block">
    <p class="trend-title">Total Job Posting on JobBoard By Occupational Sector</p>
    <p class="trend-sub">% Change in job postings since Feb 1, 2020, seasonally adjusted to Oct 8, 2021</p>
    <p class="trend-note">Job postings on JobBoard are a real-time measure of labor market activity. Only July 16, 2021, they were 36.5% above February 1, 2020, the pre-pandemic baseline, after adjusting for seasonal variation. However, job postings increased in May, June, and July at a slower pace than in March and April.</p>
  </div>

  <svg class="postings-chart" width="290" height="150" viewBox="0 0 290 150">
    <g stroke="#e2e2e2" stroke-width=".5">
      <line x1="22" y1="8" x2="288" y2="8"/><line x1="22" y1="20.1" x2="288" y2="20.1"/><line x1="22" y1="32.2" x2="288" y2="32.2"/><line x1="22" y1="44.3" x2="288" y2="44.3"/><line x1="22" y1="56.4" x2="288" y2="56.4"/><line x1="22" y1="68.5" x2="288" y2="68.5"/><line x1="22" y1="80.6" x2="288" y2="80.6"/><line x1="22" y1="92.7" x2="288" y2="92.7"/><line x1="22" y1="104.8" x2="288" y2="104.8"/><line x1="22" y1="116.9" x2="288" y2="116.9"/>
    </g>
    <g font-size="4.6" fill="#555">
      <text x="0" y="10">100%</text><text x="3" y="22">80%</text><text x="3" y="34">60%</text><text x="3" y="46">40%</text><text x="3" y="58">20%</text><text x="6" y="70">0%</text><text x="1" y="82">-20%</text><text x="1" y="94">-40%</text><text x="1" y="106">-60%</text><text x="1" y="119">-80%</text>
    </g>
    <rect x="28" y="12" width="5" height="5" fill="#1f3f8f"/><text x="36" y="16.5" font-size="5.2" fill="#333">Hospitality &amp; Tourism</text>
    <rect x="96" y="12" width="5" height="5" fill="#2e8b6f"/><text x="104" y="16.5" font-size="5.2" fill="#333">Logistic Support</text>
    <rect x="28" y="22" width="5" height="5" fill="#c33a93"/><text x="36" y="26.5" font-size="5.2" fill="#333">Loading &amp; Stocking</text>
    <rect x="96" y="22" width="5" height="5" fill="#c98a2a"/><text x="104" y="26.5" font-size="5.2" fill="#333">Retail</text>
    <g fill="none" stroke-width="1.3" stroke-linejoin="round">
      <polyline stroke="#c98a2a" points="22,68.5 35,69.7 45,86.7 55,80.6 75,71.5 95,65.5 115,62.5 135,59.4 155,59.4 175,57.6 195,53.4 215,50.4 235,47.3 255,45.5 270,45.5 285,47.3"/>
      <polyline stroke="#2e8b6f" points="22,68.5 35,70.3 45,92.7 55,86.7 75,80.6 95,77.6 115,74.6 135,71.5 155,68.5 175,62.5 195,50.4 215,44.3 235,41.3 255,35.2 270,29.2 285,26.2"/>
      <polyline stroke="#c33a93" points="22,68.5 35,69.7 45,89.7 55,83.6 75,74.6 95,68.5 115,65.5 135,62.5 155,56.4 175,50.4 195,44.3 215,35.2 235,32.2 255,23.1 270,20.1 285,15.3"/>
      <polyline stroke="#1f3f8f" points="22,68.5 35,71.5 45,104.8 55,101.8 75,95.7 95,94 115,92.7 135,91.5 155,89.7 175,86.7 195,83.6 215,77.6 235,71.5 255,65.5 270,62.5 285,59.4"/>
    </g>
    <g font-size="4.4" fill="#555">
      <text transform="translate(26 140) rotate(-60)">Feb '20</text><text transform="translate(56 140) rotate(-60)">Apr '20</text><text transform="translate(86 140) rotate(-60)">Jul '20</text><text transform="translate(116 140) rotate(-60)">Sep '20</text><text transform="translate(146 140) rotate(-60)">Dec '20</text><text transform="translate(176 140) rotate(-60)">Feb '21</text><text transform="translate(206 140) rotate(-60)">Apr '21</text><text transform="translate(236 140) rotate(-60)">Jun '21</text><text transform="translate(266 140) rotate(-60)">Aug '21</text><text transform="translate(284 140) rotate(-60)">Oct '21</text>
    </g>
  </svg>

  <svg class="incentive-chart" width="290" height="128" viewBox="0 0 290 128">
    <g stroke="#e2e2e2" stroke-width=".5">
      <line x1="16" y1="6" x2="288" y2="6"/><line x1="16" y1="25.8" x2="288" y2="25.8"/><line x1="16" y1="45.6" x2="288" y2="45.6"/><line x1="16" y1="65.4" x2="288" y2="65.4"/><line x1="16" y1="85.2" x2="288" y2="85.2"/><line x1="16" y1="105" x2="288" y2="105"/>
    </g>
    <g font-size="5" fill="#555">
      <text x="2" y="8">5%</text><text x="2" y="28">4%</text><text x="2" y="48">3%</text><text x="2" y="67">2%</text><text x="2" y="87">1%</text><text x="2" y="107">0%</text>
    </g>
    <text x="22" y="15" font-size="7.6" font-weight="700" fill="#333">More postings are advertising</text>
    <text x="22" y="24" font-size="7.6" font-weight="700" fill="#333">hiring incentives</text>
    <polyline fill="none" stroke="#1f3f8f" stroke-width="1.5" stroke-linejoin="round" points="18,69.4 25,67.4 40,65.4 60,63.4 80,59.5 95,55.5 105,53.5 112,56.5 130,55.5 150,54.5 170,53.5 190,51.5 210,47.6 230,41.6 250,33.7 265,25.8 275,19.9 285,17.9"/>
    <text x="150" y="78" font-size="7" fill="#555">Share of job postings that advertise</text>
    <text x="150" y="87" font-size="7" fill="#555">hiring incentives through July 16, 2021</text>
    <g font-size="5" font-weight="700" fill="#444" text-anchor="middle">
      <text x="20" y="120">Jul 2020</text><text x="75" y="120">Oct 2020</text><text x="135" y="120">Jan 2021</text><text x="210" y="120">Apr 2021</text><text x="278" y="120">Jul 2021</text>
    </g>
  </svg>
</section>

<!-- Slide B -->
<section class="slide slide--second">
  <div class="side-panel"></div>
  <h1 class="slide-title">SUPPLY CHAIN JOB MARKET REMAINS TIGHT</h1>
  <div class="title-rule"></div>
  <span class="page-number">6</span>
  <ul class="key-points">
    <li>We continue to see pressure and struggle to attract the talent needed to meet staffing demands in multiple markets</li>
    <li>Wage inflation in the industry continues and is amplified lack of talent to cover demand for the holiday season cycle</li>
    <li>We expect demand to remain extremely high through 2022 period due to the amount of backlog freight at the ports and missed Holiday placement of goods</li>
  </ul>

  <svg class="sector-chart" width="560" height="268" viewBox="0 0 560 268">
    <text x="41" y="10" font-size="8.4" font-weight="700" fill="#333">Some sectors are booming while others lag</text>
    <text x="41" y="21" font-size="8" fill="#555">% change in US job postings, seasonally adjusted, Oct 8, 2021</text>
    <g font-size="7" font-weight="700" fill="#c8102e" text-anchor="middle">
      <text x="62.5" y="41">9.0%</text><text x="94.5" y="51">4.1%</text><text x="125.5" y="50">6.2%</text><text x="156.5" y="49">7.5%</text>
      <text x="232.5" y="44">7.0%</text><text x="263.5" y="47">6.0%</text><text x="294.5" y="69">2.8%</text><text x="326.5" y="88">0.7%</text>
      <text x="406.5" y="41">1.6%</text><text x="437.5" y="46">2.1%</text><text x="469.5" y="78">2.4%</text>
    </g>
    <g fill="#c8102e">
      <rect x="52" y="44" width="21" height="13"/><rect x="84" y="54" width="21" height="7"/><rect x="115" y="53" width="21" height="9"/><rect x="146" y="52" width="21" height="10"/>
      <rect x="222" y="47" width="21" height="17"/><rect x="253" y="50" width="21" height="15"/><rect x="284" y="72" width="21" height="6"/><rect x="316" y="91" width="21" height="2"/>
      <rect x="396" y="44" width="21" height="11"/><rect x="427" y="49" width="21" height="13"/><rect x="459" y="81" width="21" height="17"/>
      <rect x="491" y="203" width="21" height="29"/>
    </g>
    <g fill="#a6a6a6">
      <rect x="52" y="57" width="21" height="127"/><rect x="84" y="61" width="21" height="123"/><rect x="115" y="62" width="21" height="122"/><rect x="146" y="62" width="21" height="122"/>
      <rect x="222" y="64" width="21" height="120"/><rect x="253" y="65" width="21" height="119"/><rect x="284" y="78" width="21" height="106"/><rect x="316" y="93" width="21" height="91"/>
      <rect x="396" y="55" width="21" height="129"/><rect x="427" y="62" width="21" height="122"/><rect x="459" y="98" width="21" height="86"/>
      <rect x="491" y="186" width="21" height="17"/>
    </g>
    <g font-size="4.6" fill="#333" text-anchor="middle">
      <text x="62.5" y="124">92.9%</text><text x="94.5" y="124">89.9%</text><text x="125.5" y="124">89.4%</text><text x="156.5" y="124">89%</text>
      <text x="232.5" y="124">51.4%</text><text x="263.5" y="124">50.6%</text><text x="294.5" y="124">44.4%</text><text x="326.5" y="124">38.7%</text>
      <text x="406.5" y="124">22.0%</text><text x="437.5" y="124">18.6%</text><text x="469.5" y="124">13.2%</text>
      <text x="501.5" y="197">-3.8%</text>
      <text x="501.5" y="221" fill="#fff">-3.1%</text>
    </g>
    <g font-size="4.8" fill="#fff">
      <text transform="translate(64.5 180) rotate(-90)">Human Resources</text>
      <text transform="translate(96.5 180) rotate(-90)">Production &amp; Mfg</text>
      <text transform="translate(127.5 180) rotate(-90)">Loading &amp; Stocking</text>
      <text transform="translate(158.5 180) rotate(-90)">Pharmacy</text>
      <text transform="translate(234.5 180) rotate(-90)">Driving</text>
      <text transform="translate(265.5 180) rotate(-90)">Childcare</text>
      <text transform="translate(296.5 180) rotate(-90)">Arts &amp; Entertainment</text>
      <text transform="translate(328.5 180) rotate(-90)">Food Prep &amp; Service</text>
      <text transform="translate(408.5 180) rotate(-90)">Cleaning</text>
      <text transform="translate(439.5 180) rotate(-90)">Hospitality &amp; Tourism</text>
      <text transform="translate(471.5 180) rotate(-90)">Education</text>
      <text transform="translate(503.5 180) rotate(-90)" fill="#555">Beauty &amp; Wellness</text>
    </g>
    <g stroke="#999" stroke-width=".8">
      <line x1="45" y1="186" x2="175" y2="186"/><line x1="215" y1="186" x2="345" y2="186"/><line x1="388" y1="186" x2="520" y2="186"/>
    </g>
    <g font-size="5.8" font-weight="700" fill="#c8102e" text-anchor="middle">
      <text x="110" y="196">Better than economy average</text>
      <text x="280" y="196">Similar to economy average</text>
      <text x="453" y="196">Worse than economy average</text>
    </g>
    <rect x="272" y="225" width="6" height="6" fill="#a6a6a6"/>
    <text x="281" y="230.5" font-size="5.6" fill="#555">% change since 2/1/20</text>
    <rect x="350" y="225" width="6" height="6" fill="#c8102e"/>
    <text x="359" y="230.5" font-size="5.6" fill="#555">% pt. change vs 4 weeks ago</text>
  </svg>

  <div class="brand-name">Harbor Supply Co.</div>

  <div class="trend-block">
    <p class="trend-title">Total Job Posting on JobBoard By Occupational Sector</p>
    <p class="trend-sub">% Change in job postings since Feb 1, 2020, seasonally adjusted to Oct 8, 2021</p>
    <p class="trend-note">Job postings on JobBoard are a real-time measure of labor market activity. Only July 16, 2021, they were 36.5% above February 1, 2020, the pre-pandemic baseline, after adjusting for seasonal variation. However, job postings increased in May, June, and July at a slower pace than in March and April.</p>
  </div>

  <svg class="postings-chart" width="290" height="150" viewBox="0 0 290 150">
    <g stroke="#e2e2e2" stroke-width=".5">
      <line x1="22" y1="8" x2="288" y2="8"/><line x1="22" y1="20.1" x2="288" y2="20.1"/><line x1="22" y1="32.2" x2="288" y2="32.2"/><line x1="22" y1="44.3" x2="288" y2="44.3"/><line x1="22" y1="56.4" x2="288" y2="56.4"/><line x1="22" y1="68.5" x2="288" y2="68.5"/><line x1="22" y1="80.6" x2="288" y2="80.6"/><line x1="22" y1="92.7" x2="288" y2="92.7"/><line x1="22" y1="104.8" x2="288" y2="104.8"/><line x1="22" y1="116.9" x2="288" y2="116.9"/>
      <line x1="55" y1="8" x2="55" y2="117"/><line x1="95" y1="8" x2="95" y2="117"/><line x1="135" y1="8" x2="135" y2="117"/><line x1="175" y1="8" x2="175" y2="117"/><line x1="215" y1="8" x2="215" y2="117"/><line x1="255" y1="8" x2="255" y2="117"/>
    </g>
    <g font-size="4.6" fill="#555">
      <text x="0" y="10">100%</text><text x="3" y="22">80%</text><text x="3" y="34">60%</text><text x="3" y="46">40%</text><text x="3" y="58">20%</text><text x="6" y="70">0%</text><text x="1" y="82">-20%</text><text x="1" y="94">-40%</text><text x="1" y="106">-60%</text><text x="1" y="119">-80%</text>
    </g>
    <rect x="28" y="12" width="5" height="5" fill="#1f3f8f"/><text x="36" y="16.5" font-size="5.2" fill="#333">Hospitality &amp; Tourism</text>
    <rect x="96" y="12" width="5" height="5" fill="#2e8b6f"/><text x="104" y="16.5" font-size="5.2" fill="#333">Logistic Support</text>
    <rect x="28" y="22" width="5" height="5" fill="#c33a93"/><text x="36" y="26.5" font-size="5.2" fill="#333">Loading &amp; Stocking</text>
    <rect x="96" y="22" width="5" height="5" fill="#c98a2a"/><text x="104" y="26.5" font-size="5.2" fill="#333">Retail</text>
    <g fill="none" stroke-width="1.3" stroke-linejoin="round">
      <polyline stroke="#c98a2a" points="22,68.5 35,69.7 45,86.7 55,80.6 75,71.5 95,65.5 115,62.5 135,59.4 155,59.4 175,57.6 195,53.4 215,50.4 235,47.3 255,45.5 270,45.5 285,47.3"/>
      <polyline stroke="#2e8b6f" points="22,68.5 35,70.3 45,92.7 55,86.7 75,80.6 95,77.6 115,74.6 135,71.5 155,68.5 175,62.5 195,50.4 215,44.3 235,41.3 255,35.2 270,29.2 285,26.2"/>
      <polyline stroke="#c33a93" points="22,68.5 35,69.7 45,89.7 55,83.6 75,74.6 95,68.5 115,65.5 135,62.5 155,56.4 175,50.4 195,44.3 215,35.2 235,32.2 255,23.1 270,20.1 285,15.3"/>
      <polyline stroke="#1f3f8f" points="22,68.5 35,71.5 45,104.8 55,101.8 75,95.7 95,94 115,92.7 135,91.5 155,89.7 175,86.7 195,83.6 215,77.6 235,71.5 255,65.5 270,62.5 285,59.4"/>
    </g>
    <g font-size="4.4" fill="#555">
      <text transform="translate(26 140) rotate(-60)">Feb '20</text><text transform="translate(56 140) rotate(-60)">Apr '20</text><text transform="translate(86 140) rotate(-60)">Jul '20</text><text transform="translate(116 140) rotate(-60)">Sep '20</text><text transform="translate(146 140) rotate(-60)">Dec '20</text><text transform="translate(176 140) rotate(-60)">Feb '21</text><text transform="translate(206 140) rotate(-60)">Apr '21</text><text transform="translate(236 140) rotate(-60)">Jun '21</text><text transform="translate(266 140) rotate(-60)">Aug '21</text><text transform="translate(284 140) rotate(-60)">Oct '21</text>
    </g>
  </svg>

  <svg class="incentive-chart" width="290" height="128" viewBox="0 0 290 128">
    <g stroke="#e2e2e2" stroke-width=".5">
      <line x1="16" y1="6" x2="288" y2="6"/><line x1="16" y1="25.8" x2="288" y2="25.8"/><line x1="16" y1="45.6" x2="288" y2="45.6"/><line x1="16" y1="65.4" x2="288" y2="65.4"/><line x1="16" y1="85.2" x2="288" y2="85.2"/><line x1="16" y1="105" x2="288" y2="105"/>
    </g>
    <g font-size="5" fill="#555">
      <text x="2" y="8">5%</text><text x="2" y="28">4%</text><text x="2" y="48">3%</text><text x="2" y="67">2%</text><text x="2" y="87">1%</text><text x="2" y="107">0%</text>
    </g>
    <text x="22" y="15" font-size="7.6" font-weight="700" fill="#333">More postings are advertising</text>
    <text x="22" y="24" font-size="7.6" font-weight="700" fill="#333">hiring incentives</text>
    <polyline fill="none" stroke="#1f3f8f" stroke-width="1.5" stroke-linejoin="round" points="18,69.4 25,67.4 40,65.4 60,63.4 80,59.5 95,55.5 105,53.5 112,56.5 130,55.5 150,54.5 170,53.5 190,51.5 210,47.6 230,41.6 250,33.7 265,25.8 275,19.9 285,17.9"/>
    <text x="150" y="78" font-size="7" fill="#555">Share of job postings that advertise</text>
    <text x="150" y="87" font-size="7" fill="#555">hiring incentives through July 16, 2021</text>
    <g font-size="5" font-weight="700" fill="#444" text-anchor="middle">
      <text x="20" y="120">Jul 2020</text><text x="75" y="120">Oct 2020</text><text x="135" y="120">Jan 2021</text><text x="210" y="120">Apr 2021</text><text x="278" y="120">Jul 2021</text>
    </g>
  </svg>
</section>

</body>
</html>
```